Optimization existing Business Card

I need a revision of the business card, incl. Logo Design. I am a freelancer and have my headquarters in Berlin. I develop business consulting solutions for banks, insurance and StartUp Companies. I want a simple design of the business card. The final design should professionalism and commitment and openness to communicate. I'm open minded in addition to optimizing the existing logo / business card as well on a new idea / proposal for the logo. Idea would be for example the logo of this page: http://varlow-strategic.consulting.

Target Market(s)

Consulting, Banking, Investment Banking

Industry/Entity Type

Business

Contact Information for Business Card

siehe Anhang (please take a look into the attachments, important)

Font styles to use
Sans Serif

Requirements
Must have
• Please look at my specifications exactly !! (Please see my specifications), CEO Founder not
Should not have
• No gradient !! (No overarching color gradient)

```html
<!DOCTYPE html>
<html lang="de">
<head>
<meta charset="utf-8">
<title>Halvorsen Consulting – Visitenkarte</title>
<link rel="stylesheet" href="https://fonts.googleapis.com/css2?family=Open+Sans:wght@400;600;700&display=swap">
<style>
  :root {
    --navy: #0b2a55;
    --sky: #14a6e0;
    --ink: #141414;
    --paper: #ffffff;
  }
  * { margin: 0; padding: 0; box-sizing: border-box; }
  html, body { width: 1200px; height: 806px; overflow: hidden; background: var(--paper); }
  .card {
    position: relative;
    width: 1200px;
    height: 806px;
    background: var(--paper);
    font-family: "Open Sans", sans-serif;
    color: var(--ink);
    overflow: hidden;
  }
  .wave { position: absolute; inset: 0; width: 1200px; height: 806px; }
  .wave .band { fill: var(--navy); }
  .wave .swoosh { fill: var(--sky); }

  .brand {
    position: absolute;
    left: 72px;
    top: 124px;
    display: flex;
    align-items: center;
    gap: 22px;
  }
  .brand-dot {
    width: 112px;
    height: 112px;
    border-radius: 50%;
    background: var(--navy);
    flex: none;
  }
  .brand-name {
    color: var(--navy);
    font-weight: 700;
    font-size: 44px;
    line-height: 48px;
    letter-spacing: -0.5px;
  }
  .brand-divider {
    position: absolute;
    left: 539px;
    top: 136px;
    width: 3px;
    height: 101px;
    background: var(--sky);
  }
  .services {
    position: absolute;
    left: 557px;
    top: 142px;
    list-style: none;
    color: var(--navy);
    font-size: 20px;
    line-height: 29.5px;
    text-transform: uppercase;
    letter-spacing: -0.2px;
  }

  .address {
    position: absolute;
    left: 73px;
    top: 408px;
    font-style: normal;
    font-size: 27px;
    line-height: 40px;
  }
  .contacts {
    position: absolute;
    left: 72px;
    top: 518px;
    list-style: none;
    font-size: 27px;
    line-height: 41px;
  }
  .contacts li { display: flex; align-items: center; gap: 20px; }
  .contacts svg { width: 30px; height: 26px; flex: none; fill: var(--sky); }

  .person {
    position: absolute;
    right: 70px;
    top: 402px;
    text-align: right;
  }
  .person-name {
    color: var(--sky);
    font-weight: 700;
    font-size: 36px;
    line-height: 44px;
  }
  .person-role {
    font-size: 26px;
    line-height: 40px;
    margin-top: 2px;
  }
  .website {
    position: absolute;
    right: 70px;
    top: 716px;
    color: var(--paper);
    font-size: 27px;
    line-height: 40px;
  }
</style>
</head>
<body>
<div class="card">
  <svg class="wave" viewBox="0 0 1200 806" aria-hidden="true">
    <path class="swoosh" d="M160,703 C600,690 950,640 1200,572 L1200,625 C1000,668 650,698 160,703 Z"/>
    <path class="band" d="M0,713 L400,713 C800,705 1050,670 1200,639 L1200,806 L0,806 Z"/>
  </svg>

  <div class="brand">
    <span class="brand-dot"></span>
    <div class="brand-name">halvorsen<br>consulting</div>
  </div>
  <span class="brand-divider"></span>
  <ul class="services">
    <li>Unternehmensberatung</li>
    <li>Banking</li>
    <li>Business Coaching</li>
  </ul>

  <address class="address">Lindenallee 48,<br>10115 Berlin, Germany</address>

  <ul class="contacts">
    <li>
      <svg viewBox="0 0 30 26" aria-label="Telefon"><path d="M7 2 L11 2 L13 8 L10 10 C11.5 13.5 14 16 17.5 17.5 L19.5 14.5 L25.5 16.5 L25.5 20.5 C25.5 22.5 24 24 22 24 C12 23.5 4 15.5 3.5 5.5 C3.5 3.5 5 2 7 2 Z"/></svg>
      <span>+49 (0) 30 55501287</span>
    </li>
    <li>
      <svg viewBox="0 0 30 26" aria-label="Mobil"><path d="M10 1 H20 A2 2 0 0 1 22 3 V23 A2 2 0 0 1 20 25 H10 A2 2 0 0 1 8 23 V3 A2 2 0 0 1 10 1 Z M10.5 4 V13 H19.5 V4 Z M11 15.5 H13 V17 H11 Z M14 15.5 H16 V17 H14 Z M17 15.5 H19 V17 H17 Z M11 18.5 H13 V20 H11 Z M14 18.5 H16 V20 H14 Z M17 18.5 H19 V20 H17 Z"/></svg>
      <span>+49 (0) 176 55503194</span>
    </li>
    <li>
      <svg viewBox="0 0 30 26" aria-label="E-Mail"><path d="M3 5 H27 L15 15 Z M3 7.5 L11 14 L3 21 Z M27 7.5 V21 L19 14 Z M12.5 15.3 L15 17.4 L17.5 15.3 L26 22 H4 Z"/></svg>
      <span>jh@halvorsen-consulting.de</span>
    </li>
  </ul>

  <div class="person">
    <div class="person-name">Jonas Halvorsen</div>
    <div class="person-role">Management Consultant</div>
  </div>

  <div class="website">www.halvorsen-consulting.de</div>
</div>
</body>
</html>
```